Natural Essential Oil Packaging

We would like you to develop a line of packaging for natural essential oil products from a company named “Lan Suoi Bich.”
List of items to be designed:
- 01 Company logo
- Air freshener (spray) product: 01 Package design + 01 label design
- 02 essential oil (glass containers) variants: 02 Label designs + 01 “how to use” attached instruction tag
Description:
A. Company logo:
- Company name: Lan Suoi Bich (“Tram” is the Vietnamese name for melaleuca);
- symbolizing "pure, natural, untouched, Lan Suoi Bich, essential,";
- should consist of text and graphic;
- should suggest a stylized drop of oil;
B. Air freshener (spray) product (Packaging and label design)
a. Product description
- Oil extracted from the unique Vietnamese cajeput trees
- Strength: pleasant aroma, air cleansing, virus and bacteria cleaning and prevention, insect expelling
- Used for: air refreshing, relaxing, spa-effect, air cleaning, air-born virus prevention (flu virus), insect expelling
- Application: air spray
b. Package to design: 170ml glass spray bottle
c. Label text for design: brand name: Vorenta + variant name “Lemongrass” + Air Freshener + Melaleuca Essential Oil
C. 02 essential oil (glass containers) variants (Label and Instrution Tag designs)
a. Production description:
i. 02 product variant under the brand name Tuscavi
1 - Vietnamese Cajeput Oil: Special breed of cajeput only found in Vietnam, known for amazingly pleasant fragrance giving senses of relaxation, refreshment, peace while at the same time, driving off potential disease carrying elements in the air
2 - Australian tea trea oil: Australian breed of malaleuca known for effective healing of skin from various types of infection, skin protection and highly effective oral hygiene
ii. Product values:
1. 100% pure oil, 100% organic, 100% environment and human friendly, NO chemical
2. aiming to promote human’s well being, health, nature sustainability, improve living environment
3. both products are about nurturing, uplifting, healing and recovering
4. both place their values on authenticity, originality, nature, exotic natural ingredients, green and organic life style
5. both have zero chemical and artificial substance hence 100% safe for long time and frequent usage
iii. SKU: 10ml glass container
iv. Application: for both topical and oral use
b. Label text for design:
i. brand name: Tuscavi + variant name: Cajeput Oil / Tea Tree Oil
D. Creative elements are suggested to be communicating organicity, understated premiumness, nature, lightness, nurturing
PLEASE SEE ATTACHED FILES FOR BETTER BRIEF DETAILS AND LAYOUTS.

```html
<!DOCTYPE html>
<html lang="en">
<head>
<meta charset="utf-8">
<title>Tuscavi Vietnamese Tea Tree Oil – Label</title>
<link href="https://fonts.googleapis.com/css2?family=Montserrat:ital,wght@0,500;0,600;0,700;0,800;1,300;1,600;1,700&display=swap" rel="stylesheet">
<style>
  :root {
    --sage: #9fb6a6;
    --paper: #ffffff;
    --wine: #7a1722;
    --leaf: #3aa64a;
    --leaf-deep: #4f8f55;
    --lime: #8cbf3f;
    --seal: #8b8f6c;
    --ink-light: #ffffff;
  }
  * { margin: 0; padding: 0; box-sizing: border-box; }
  html, body { width: 1200px; height: 1003px; overflow: hidden; background: var(--paper); }
  body { position: relative; font-family: "Montserrat", Arial, sans-serif; }

  .wrapper-shape { position: absolute; left: 0; width: 1200px; }
  .wrapper-shape--top { top: 0; height: 315px; }
  .wrapper-shape--bottom { top: 683px; height: 320px; }
  .wrapper-shape path, .wrapper-shape rect, .wrapper-shape ellipse { fill: var(--sage); }

  .story {
    position: absolute; left: 176px; top: 88px; width: 400px;
    color: var(--ink-light); font-style: italic; font-weight: 300;
    font-size: 20.5px; line-height: 30px; text-align: center;
  }
  .ingredients { position: absolute; left: 608px; top: 42px; width: 420px; text-align: center; }
  .ingredients__title { color: var(--wine); font-weight: 700; font-size: 17px; letter-spacing: .3px; }
  .ingredients__list {
    margin-top: 12px; color: var(--ink-light); font-weight: 700; font-style: italic;
    font-size: 13.5px; line-height: 19px;
  }
  .maker-name {
    position: absolute; left: 700px; top: 198px; width: 240px; text-align: center;
    font-weight: 800; font-size: 24px; color: var(--wine);
  }

  .brand {
    position: absolute; left: 0; top: 318px; width: 1200px; text-align: center;
    font-weight: 700; font-size: 168px; line-height: 1; color: var(--leaf-deep); letter-spacing: 4px;
  }
  .variant {
    position: absolute; left: 200px; top: 545px; width: 920px; text-align: center;
    font-weight: 800; font-size: 60px; color: var(--leaf); letter-spacing: .5px;
  }

  .panel {
    position: absolute; top: 707px; height: 268px;
    border: 2px solid var(--wine); text-align: center;
  }
  .panel--directions { left: 163px; width: 420px; }
  .panel--seal { left: 614px; width: 418px; }
  .directions__title { margin-top: 8px; color: var(--ink-light); font-weight: 700; font-size: 16.5px; }
  .directions__text {
    margin: 20px auto 0; width: 405px; color: var(--wine); font-weight: 700; font-style: italic;
    font-size: 15.5px; line-height: 23px;
  }
  .certificate { position: absolute; left: 153px; top: 155px; width: 104px; height: 104px; }
  .certificate circle { fill: var(--seal); }

  .mini-brand {
    margin-top: 60px; font-weight: 700; font-size: 64px; line-height: 1; color: var(--leaf-deep); letter-spacing: 2px;
  }
  .mini-variant { margin-top: 4px; font-weight: 700; font-size: 25px; color: var(--lime); }
  .usage {
    position: absolute; left: 0; bottom: 20px; width: 100%;
    color: var(--ink-light); font-weight: 700; font-style: italic; font-size: 19px;
  }
</style>
</head>
<body>
  <svg class="wrapper-shape wrapper-shape--top" viewBox="0 0 1200 315" aria-hidden="true">
    <rect x="118" y="0" width="966" height="313" rx="28"/>
    <ellipse cx="72" cy="78" rx="76" ry="70"/>
    <ellipse cx="72" cy="232" rx="76" ry="70"/>
    <ellipse cx="1128" cy="78" rx="76" ry="70"/>
    <ellipse cx="1128" cy="232" rx="76" ry="70"/>
    <rect x="90" y="70" width="60" height="170"/>
    <rect x="1050" y="70" width="60" height="170"/>
  </svg>

  <p class="story">This Australian breed of melaleuca is is known for its effective healing properties, including skin ailments and infections. It is also highly as an oral hygiene product.</p>

  <div class="ingredients">
    <h2 class="ingredients__title">INGREDIENTS</h2>
    <p class="ingredients__list">Water, alcohol, melaleuca (tea) tree oil, Water, alcohol, melaleuca (tea) tree oil Water, alcohol, melaleuca (tea) tree oil</p>
  </div>
  <div class="maker-name">Lan Suoi Bich</div>

  <h1 class="brand">Tuscavi</h1>
  <p class="variant">Vietnamese Tea Tree Oil</p>

  <svg class="wrapper-shape wrapper-shape--bottom" viewBox="0 0 1200 320" aria-hidden="true">
    <rect x="118" y="2" width="966" height="316" rx="28"/>
    <ellipse cx="72" cy="82" rx="76" ry="70"/>
    <ellipse cx="72" cy="238" rx="76" ry="70"/>
    <ellipse cx="1128" cy="82" rx="76" ry="70"/>
    <ellipse cx="1128" cy="238" rx="76" ry="70"/>
    <rect x="90" y="75" width="60" height="170"/>
    <rect x="1050" y="75" width="60" height="170"/>
  </svg>

  <section class="panel panel--directions">
    <h3 class="directions__title">Directions for Use:</h3>
    <p class="directions__text">Place three drops of Tuscavi Vietnamese Tea Tree Oil onto tongue and swallow or apply to affected skin.</p>
    <svg class="certificate" viewBox="0 0 104 104" role="img" aria-label="Organic certification seal">
      <circle cx="52" cy="52" r="50"/>
    </svg>
  </section>

  <section class="panel panel--seal">
    <div class="mini-brand">Tuscavi</div>
    <div class="mini-variant">Vietnamese Tea Tree Oil</div>
    <p class="usage">for topical and oral use</p>
  </section>
</body>
</html>
```